Flyer Design For Building & Decorating Company

We need an A6 double-sided colour flyer for a letter-box marketing campaign. We are a building and decorating company based in West London. We saw a flyer that we liked and have attached it as an example of the sort of thing we're looking for (see attached files Example A6 Flyer - Front.png and Example A6 Flyer - Back.png). Please note that we're not expecting the designer to slavishly follow this design, more to use it as a jumping-off point.

The design must incorporate a strong call to action, e.g., Call Us For A Free, No-Obligation Quote.

The textual information that must be included in the flyer (contact methods, tagline, services, etc.) are included in the attached file Flyer Text.docx.

Also included as attachments are a selection of images used on our website (files bathroom.png, carpentry.png, decorating.jpg,
flooring.jpg, painting_decorating.jpg, repointing.jpg and work_ on_scaffold.jpg). Please include these images on the flyer (at least one image on each side), or use stock images if any of these are unsuitable.

The company logo will also need to be included in the flyer - see attached file logo.png

The images on our website have all had to be re-sized from the originals. I've attached a number of the original images to this brief, as these are the highest resolution versions of the images that we have. I would ask that you use the versions attached to the brief, but if you feel that other images from our website would work better on your flyer design, please let me know and I'll attach them to this brief.

Finally, we've attached guideline notes from our printer (see attached file Printer's Requirements.docx) - please ensure these are adhered to where relevant.

Target Market(s)

People in West London who require building or decorating work to be done on their properties.

Industry/Entity Type

Marketing

Requirements
Must have
• A6 double-sided colour flyer using the text we provided and some of the images provided.

The call to action must be prominent and eye-catching, as the only purpose of the flyer is to get recipients to contact our company for a quote.

```html
<!DOCTYPE html>
<html lang="en">
<head>
<meta charset="utf-8">
<title>Oakbridge Renovations – A6 Flyer</title>
<link href="https://fonts.googleapis.com/css2?family=Roboto+Condensed:wght@400;700&display=swap" rel="stylesheet">
<style>
  :root{
    --sky:#1aa5e5;
    --sky-pale:#cfe9f7;
    --navy:#1c2b4f;
    --navy-soft:#3b4f86;
    --gold:#f6c21c;
    --paper:#ffffff;
    --backdrop:#e6e7e8;
    --ink:#1e2233;
  }
  *{box-sizing:border-box;margin:0;padding:0}
  html,body{width:1200px;height:844px;overflow:hidden;background:var(--backdrop)}
  body{font-family:"Roboto Condensed",Arial,sans-serif;font-weight:700}
  .sheet{position:absolute;left:0;top:0;width:1038px;height:730px;transform:scale(1.1561);transform-origin:0 0}
  .side{position:absolute;top:16px;width:496px;height:698px;overflow:hidden;background:var(--paper)}
  .front{left:16px}
  .back{left:527px}

  /* front */
  .front-art{position:absolute;inset:0}
  .tagline{position:absolute;left:38px;top:24px;color:var(--navy-soft);font-size:13px;line-height:15px}
  .brand{position:absolute;left:296px;top:56px;width:130px;display:flex;align-items:center;gap:6px;color:var(--navy);font-size:18px}
  .brand-dot{width:12px;height:12px;background:var(--gold)}
  .services-title{position:absolute;left:26px;top:422px;width:150px;height:28px;background:var(--navy);border-right:4px solid var(--navy-soft);border-bottom:3px solid var(--navy-soft);color:#fff;font-size:19px;padding:2px 10px}
  .services-list{position:absolute;left:37px;top:464px;list-style:none;color:#fff;font-size:14.5px;line-height:20.1px}
  .cta{position:absolute;left:200px;top:537px;width:290px;text-align:center;color:#fff}
  .cta-head{font-size:19.5px;line-height:24px}
  .cta-phone{font-size:26px;line-height:30px}
  .cta-web{font-size:16px;line-height:20px;margin-top:2px}

  /* back */
  .offer{position:absolute;left:35px;top:14px;width:205px;color:var(--ink)}
  .offer-group{margin-bottom:12px}
  .offer-group h3{font-size:16.5px;line-height:18px;color:var(--navy)}
  .offer-group ul{list-style:none;font-size:12.2px;line-height:14.3px}
  .offer-group li{padding-left:10px;text-indent:-10px}
  .offer-group li::before{content:"· "}
  .photo{position:absolute;left:246px;width:110px}
  .testimonial{position:absolute;left:365px;top:14px;width:112px;font-size:8.6px;line-height:10.9px;color:var(--ink)}
  .testimonial .mark{font-size:18px;line-height:8px;vertical-align:-6px}
  .quote-box{position:absolute;left:246px;top:520px;width:229px;height:31px;border-top:3px solid var(--ink);border-bottom:2px solid var(--ink);text-align:center;font-size:19px;line-height:26px;color:var(--ink)}
  .contact-band{position:absolute;left:0;top:572px;width:496px;height:126px;background:var(--sky)}
  .contact-details{position:absolute;left:35px;top:24px;color:#fff;font-size:11.2px;line-height:13.2px}
  .contact-prompt{position:absolute;left:296px;top:0;width:200px;height:126px;border-left:4px solid #fff;border-top:4px solid #fff;border-top-left-radius:34px;padding:20px 0 0 18px;color:#fff;font-size:14.5px;line-height:17.6px;background:var(--sky)}
</style>
</head>
<body>
<div class="sheet">

  <section class="side front">
    <svg class="front-art" width="496" height="698" viewBox="0 0 496 698">
      <defs>
        <linearGradient id="skyFade" x1="0" y1="0" x2="0" y2="1">
          <stop offset="0" stop-color="#ffffff"/>
          <stop offset="0.55" stop-color="#d7ecf8"/>
          <stop offset="1" stop-color="#1aa5e5"/>
        </linearGradient>
        <linearGradient id="roomTones" x1="0" y1="0" x2="1" y2="1">
          <stop offset="0" stop-color="#e9eef2"/>
          <stop offset="0.45" stop-color="#3b5f8e"/>
          <stop offset="1" stop-color="#6a4a33"/>
        </linearGradient>
      </defs>
      <rect width="496" height="698" fill="var(--sky)"/>
      <polygon points="0,0 496,0 496,150 0,190" fill="url(#skyFade)"/>
      <polygon points="0,185 496,140 496,325 0,460" fill="url(#roomTones)" role="img" aria-label="Photo of a renovated bathroom with blue panelling, radiator and wooden floor"/>
      <polygon points="0,180 496,134 496,142 0,190" fill="var(--gold)"/>
      <polygon points="0,455 496,320 496,330 0,467" fill="var(--gold)"/>
    </svg>
    <p class="tagline">West London Builders &amp; Decorators<br>Quality Renovations At Affordable Prices</p>
    <div class="brand"><span class="brand-dot"></span>Oakbridge</div>

    <h2 class="services-title">Our services</h2>
    <ul class="services-list">
      <li>Bathrooms/Kitchens</li>
      <li>Tiling</li>
      <li>Painting/Decorating</li>
      <li>Plastering</li>
      <li>Carpentry</li>
      <li>Flooring</li>
      <li>Plumbing</li>
      <li>Electrical Works</li>
      <li>Brickwork</li>
      <li>General Repairs</li>
    </ul>

    <div class="cta">
      <p class="cta-head">CALL US FOR A FREE QUOTE</p>
      <p class="cta-phone">0208 555 0142</p>
      <p class="cta-phone">07700 900318</p>
      <p class="cta-web">hello@oakbridge-reno.co.uk</p>
      <p class="cta-web">www.oakbridge-reno.co.uk</p>
    </div>
  </section>

  <section class="side back">
    <div class="offer">
      <div class="offer-group">
        <h3>Bathroom/Kitchen:</h3>
        <ul><li>Complete/Partial Fixings</li><li>Tiling</li><li>Sink/Bath/Radiator</li><li>Tap Repairs/Replace</li><li>Fit Washing Machine/ Dishwasher</li></ul>
      </div>
      <div class="offer-group">
        <h3>Decorating:</h3>
        <ul><li>Complete/Partial Works</li><li>Lining/Wallpaper</li><li>Painting Inside/Outside</li><li>Plastering/Skimming</li><li>Rectify Damage/ Freshen Paintwork</li></ul>
      </div>
      <div class="offer-group">
        <h3>Carpentry:</h3>
        <ul><li>Wardrobes/Cupboards</li><li>Shelving/Skirting</li><li>Doors/Windows</li><li>Kitchen/Bathroom Suites</li><li>Wooden Floor/Laminate</li></ul>
      </div>
      <div class="offer-group">
        <h3>Maintenance/Repairs:</h3>
        <ul><li>Reseal Bath/Shower</li><li>Fit Shelves</li><li>Electrics - Complete/Partial</li><li>Sash/Gutter/Roof Repairs</li><li>Lots more ...</li></ul>
      </div>
      <div class="offer-group">
        <h3>Landscaping/Roof/<br>Work On High Ladders:</h3>
        <ul><li>Fencing/Paving/Decking</li><li>Work On High Ladders/Scaffold</li><li>Tree Cutting/Removal</li><li>Roofing - New/Repair</li></ul>
      </div>
    </div>

    <div class="photo" style="top:17px;height:77px;background:linear-gradient(135deg,#c9a27a,#efe6da)" role="img" aria-label="Carpenter assembling a cabinet"></div>
    <div class="photo" style="top:104px;height:76px;background:linear-gradient(160deg,#f2efe9,#b8aa97)" role="img" aria-label="Freshly decorated ceiling and alcove"></div>
    <div class="photo" style="top:191px;height:77px;background:linear-gradient(135deg,#e9e4da,#c99a7c)" role="img" aria-label="Hands fitting decorative coving"></div>
    <div class="photo" style="top:277px;height:77px;background:linear-gradient(135deg,#d6a86a,#f3e2c4)" role="img" aria-label="Laying laminate flooring"></div>
    <div class="photo" style="top:364px;height:132px;background:linear-gradient(135deg,#a8473a,#c9775f)" role="img" aria-label="Repointed red brick wall"></div>
    <div class="photo" style="left:365px;top:364px;height:132px;background:linear-gradient(180deg,#dfe6ee,#9aa0a6)" role="img" aria-label="Scaffolding on a white house"></div>

    <p class="testimonial"><span class="mark">"</span>Martin came to the rescue after my first builder walked off site (daunted perhaps by the scope of work required - new kitchen, bathrooms, patio, new fireplace, a host of minor internal and external repairs, and total redecoration). His team began immediately, worked a minimum 9hr. day (sometimes 12!!), were punctual, polite &amp; thoroughly pleasant to have around the house, and completed the project to my entire satisfaction. There was nothing I could fault because if any problems cropped up during the job they were attended to, without complaint, at once. After 40 years experience as a Chartered Surveyor this is the best service I have ever encountered from a local builder. Graham P., Ealing <span class="mark">"</span></p>

    <p class="quote-box">No Obligation Quote</p>

    <div class="contact-band">
      <p class="contact-details">Oakbridge Renovations<br>14 Linden Grove, Ealing, London W5 9QT<br>Tel: 0208 555 0142, Mobile: 07700 900318<br>Email: hello@oakbridge-reno.co.uk<br>Web: www.oakbridge-reno.co.uk</p>
      <p class="contact-prompt">Find Out<br>How We Can Help With<br>Your Building And<br>Decorating Needs</p>
    </div>
  </section>

</div>
</body>
</html>
```